Logo redesign & Stationery Design Project

We need a logo redesign for our company.

We also require the following stationary with the new logo:
*letterhead
*With compliments slips
*business card
*envelopes

We would like to maintain our current colours of navy blue and gold. We would like to maintain the wording on the back of our current business card.

Our existing letterhead and business card is attached.

Target Market(s)

Medical Professionals, Pharmacists, Lawyers

Industry/Entity Type

Business

Requirements
Must have
• See attached business card and letterhead, as all details on these documents need to be included.

```html
<!DOCTYPE html>
<html lang="en">
<head>
<meta charset="utf-8">
<title>HollisGrange Financial Services – Letterhead</title>
<link rel="stylesheet" href="https://fonts.googleapis.com/css2?family=Open+Sans:wght@300;400&family=PT+Sans:wght@400&display=swap">
<style>
  :root {
    --navy: #1c3f6e;
    --gold: #a0894d;
    --ink: #2b2b2b;
    --muted: #6d6d6d;
    --paper: #ffffff;
    --backdrop: #e1e1e1;
  }
  * { box-sizing: border-box; margin: 0; padding: 0; }
  html, body { width: 1200px; height: 900px; overflow: hidden; }
  body {
    background: var(--backdrop);
    position: relative;
    font-family: "Open Sans", Arial, sans-serif;
  }
  .letterhead {
    position: absolute;
    left: 389px; top: 65px;
    width: 613px; height: 791px;
    background: var(--paper);
  }
  .brand {
    position: absolute;
    left: 36px; top: 58px;
    color: var(--navy);
    font-family: "Open Sans", Arial, sans-serif;
    font-weight: 400;
    display: flex; align-items: center; gap: 8px;
  }
  .brand-mark { width: 16px; height: 16px; background: var(--navy); flex: none; }
  .brand-name { font-size: 17px; line-height: 1.1; letter-spacing: 0.3px; }
  .brand-tagline { display: block; font-size: 7px; letter-spacing: 4.2px; margin-top: 2px; }
  .contact {
    position: absolute; top: 57px;
    font-size: 9.2px; line-height: 11.6px; font-weight: 300;
    color: var(--muted);
  }
  .contact--office { left: 298px; }
  .contact--postal { left: 443px; }
  .contact .label { color: var(--gold); font-weight: 400; }
  .letter-body {
    position: absolute;
    left: 94px; top: 259px; width: 446px;
    font-family: "PT Sans", Tahoma, sans-serif;
    font-size: 9.7px; line-height: 11.6px;
    color: var(--ink);
    text-align: justify; hyphens: auto;
  }
  .letter-body p + p { margin-top: 11.6px; }
  .signature {
    position: absolute; left: 99px; top: 565px;
    width: 96px; height: 72px;
    background: linear-gradient(135deg, #f2f2f2, #dcdcdc);
  }
  .licence {
    position: absolute; left: 36px; top: 757px;
    font-size: 6.4px; font-weight: 300; color: var(--muted);
  }
  .rule-gold {
    position: absolute; left: 0; top: 772px; width: 100%; height: 2px;
    background: var(--gold);
  }
  .footer-band {
    position: absolute; left: 0; top: 776px; width: 100%; height: 15px;
    background: var(--navy);
  }
  .footer-band .web {
    position: absolute; left: 19px; top: 2px;
    font-size: 7.6px; font-weight: 300; color: #ffffff;
  }
</style>
</head>
<body>
  <main class="letterhead">
    <div class="brand">
      <span class="brand-mark"></span>
      <div class="brand-name">HollisGrange<span class="brand-tagline">Financial Services</span></div>
    </div>

    <address class="contact contact--office" style="font-style:normal">
      <span class="label">ABN</span> 31852407196<br>
      Suite 4, 118-120 Harbour Road<br>
      Westbrook NSW 2231
    </address>
    <address class="contact contact--postal" style="font-style:normal">
      PO BOX 4820 Elmwood NSW 2231<br>
      <span class="label">T.</span> 02 9000 4410 &nbsp;<span class="label">F.</span> 02 9000 4411<br>
      <span class="label">E.</span> admin@hollisgrange.com.au
    </address>

    <section class="letter-body">
      <p>In dui turpis, varius vitae, tincidunt id, consequat ut, leo. Donec tincidunt tristique odio. Nulla erat felis, euismod nec, fringilla non, aliquet et, magna. Nulla at magna quis nisi pretium vehicula. Pellentesque habitant morbi tristique senectus et netus et malesuada fames ac turpis egestas. Class aptent taciti sociosqu ad litora torquent per conubia nostra, per inceptos himenaeos. In vel quam. Phasellus varius convallis purus. In non turpis. Nam sed risus. Etiam non neque at nisl gravida porttitor. Donec leo dolor, feugiat ut, pharetra et, porttitor a, metus. Suspendisse laoreet magna vel elit. Ut est augue, fermentum ac, molestie at, vestibulum et, urna.</p>
      <p>Nunc purus. Cras auctor. In ornare neque id ipsum. Nulla tincidunt, diam sit amet viverra euismod, sapien augue fringilla neque, at pellentesque felis tortor vel enim. Etiam dignissim. Sed a tortor vel nisl euismod ultricies. Donec molestie congue lectus. Integer sed turpis a tortor imperdiet consequat. Maecenas molestie placerat urna. Sed pede enim, sollicitudin nec, pretium nec, sollicitudin a, felis. In hac habitasse platea dictumst. Nam facilisis, tellus non scelerisque placerat, turpis turpis semper ante, euismod imperdiet augue nisi et neque. Vivamus tincidunt.</p>
      <p>Nulla lobortis ultricies nulla. Pellentesque purus mi, consequat quis, hendrerit sed, imperdiet non, eros. Nullam urna est, vehicula nec, cursus nec, dignissim sit amet, risus. Duis molestie, tellus sit amet laoreet ullamcorper, urna nisi fringilla ante, at rhoncus justo dolor vel dui. Nam hendrerit luctus lorem. Aenean tempor, metus vel posuere gravida, arcu nunc imperdiet tellus, ut blandit sem magna a turpis. Vivamus in neque. Lorem ipsum dolor sit amet, consectetuer adipiscing elit. Duis tristique tortor id nisl feugiat posuere. Maecenas posuere nisi ac risus. Nunc hendrerit. Praesent porta tempus ligula. Morbi in leo. Curabitur sapien nulla, cursus eget, faucibus in, porttitor et, odio. Praesent sed justo sed arcu commodo feugiat. Duis facilisis nulla ut eros. Cras libero. Donec mollis consectetuer metus. Praesent odio.</p>
    </section>

    <div class="signature" role="img" aria-label="Handwritten signature of the sender"></div>

    <p class="licence">Corporate Authorised Representative of Northgate Advisory Group AFSL 100245</p>
    <div class="rule-gold"></div>
    <footer class="footer-band"><span class="web">www.hollisgrange.com.au</span></footer>
  </main>
</body>
</html>
```